Clean and modern business cards

Looking for an updated business card design for my dental office “corvanta dental” . Looking for a modern clean / sleek design . I’m thinking black background but open to seeing other options . One side needs to have an appointment card . Card needs to have logo, dentist name , phone, email , address . I’ve attached couple of cards I thought were cool as well as my logo
Target Market(s)
Dental patients
Industry/Entity Type
Dentistry
Contact Information for Business Card
Phone email address

```html
<!DOCTYPE html>
<html lang="en">
<head>
<meta charset="utf-8">
<title>Corvanta Dental – Business Card</title>
<link rel="stylesheet" href="https://fonts.googleapis.com/css2?family=Marcellus&display=swap">
<style>
  :root {
    --stage: #2a2a2b;
    --card: #060606;
    --ink: #f4f4f4;
    --muted: #9a9a9a;
    --accent-yellow: #f2c73d;
    --accent-orange: #e8582a;
    --accent-green: #9cc43c;
    --rule-brown: #6a3b26;
    --deco-a: #1d2a3a;
    --deco-b: #2a1d33;
  }
  * { box-sizing: border-box; margin: 0; padding: 0; }
  html, body { width: 1200px; height: 900px; overflow: hidden; }
  body {
    background: var(--stage);
    font-family: "Marcellus", "Optima", serif;
    color: var(--ink);
    display: flex;
    justify-content: center;
    align-items: center;
    gap: 80px;
  }
  .card {
    position: relative;
    width: 400px;
    height: 700px;
    background: var(--card);
    overflow: hidden;
    box-shadow: 0 12px 30px rgba(0,0,0,.45);
  }
  .card__backdrop {
    position: absolute;
    left: 0; right: 0; top: 0;
    height: 300px;
    background: radial-gradient(ellipse at 50% 35%, var(--deco-a) 0%, var(--deco-b) 35%, rgba(6,6,6,0) 70%);
    opacity: .8;
  }
  .brand {
    position: absolute;
    left: 0; right: 0;
    display: flex;
    flex-direction: column;
    align-items: center;
    gap: 14px;
  }
  .brand__dot {
    width: 26px; height: 26px;
    border-radius: 50%;
    background: var(--accent-yellow);
  }
  .brand__name {
    font-size: 30px;
    letter-spacing: 6px;
    text-transform: uppercase;
    color: var(--ink);
  }
  /* front */
  .card--front .brand { top: 380px; }
  .front__rule {
    position: absolute;
    left: 40px; right: 40px; top: 540px;
    height: 1px;
    background: var(--rule-brown);
  }
  .front__name {
    position: absolute;
    left: 0; right: 0; top: 580px;
    text-align: center;
    font-size: 26px;
    letter-spacing: 1px;
    text-transform: uppercase;
  }
  /* back */
  .card--back .card__backdrop { height: 240px; }
  .card--back .brand { top: 70px; }
  .contact {
    position: absolute;
    left: 0; right: 0; top: 210px;
    list-style: none;
    display: flex;
    flex-direction: column;
    align-items: center;
    gap: 10px;
    font-size: 19px;
  }
  .contact__item { display: flex; align-items: flex-start; gap: 9px; }
  .contact__icon { width: 17px; height: 17px; margin-top: 3px; flex: none; }
  .contact__address { line-height: 1.25; }
  .appointment__lead {
    position: absolute;
    left: 0; right: 0; top: 415px;
    text-align: center;
    color: var(--accent-green);
    font-size: 20px;
  }
  .appointment__band {
    position: absolute;
    left: 0; right: 0; top: 455px;
    height: 110px;
    background: var(--accent-yellow);
    border-top: 3px solid var(--accent-orange);
    border-bottom: 3px solid var(--accent-orange);
    padding: 22px 32px 0;
    color: #1a1a1a;
    font-size: 20px;
  }
  .appointment__field { display: flex; align-items: flex-end; gap: 10px; height: 32px; }
  .appointment__field--time { padding-left: 70px; }
  .appointment__line { flex: 1; border-bottom: 1.5px solid #1a1a1a; margin-bottom: 5px; }
  .appointment__note {
    position: absolute;
    left: 30px; right: 30px; top: 590px;
    text-align: center;
    color: var(--accent-green);
    font-size: 18px;
    line-height: 1.35;
  }
</style>
</head>
<body>
  <section class="card card--front">
    <div class="card__backdrop" role="img" aria-label="Soft coloured backdrop decoration"></div>
    <div class="brand">
      <span class="brand__dot"></span>
      <span class="brand__name">Corvanta Dental</span>
    </div>
    <div class="front__rule"></div>
    <p class="front__name">Dr. Lucan Verhoeve</p>
  </section>

  <section class="card card--back">
    <div class="card__backdrop" role="img" aria-label="Soft coloured backdrop decoration"></div>
    <div class="brand">
      <span class="brand__dot"></span>
      <span class="brand__name">Corvanta Dental</span>
    </div>
    <ul class="contact">
      <li class="contact__item">
        <svg class="contact__icon" viewBox="0 0 24 24" fill="var(--accent-yellow)"><path d="M6.6 10.8a15 15 0 0 0 6.6 6.6l2.2-2.2c.3-.3.7-.4 1-.2 1.1.4 2.3.6 3.6.6.6 0 1 .4 1 1V20c0 .6-.4 1-1 1A17 17 0 0 1 3 4c0-.6.4-1 1-1h3.5c.6 0 1 .4 1 1 0 1.3.2 2.5.6 3.6.1.3 0 .7-.2 1z"/></svg>
        <span>(204) 555 - 0142</span>
      </li>
      <li class="contact__item">
        <svg class="contact__icon" viewBox="0 0 24 24" fill="none" stroke="var(--accent-yellow)" stroke-width="2"><circle cx="12" cy="12" r="9"/><path d="M3 12h18M12 3c3 3 3 15 0 18M12 3c-3 3-3 15 0 18"/></svg>
        <span>corvantadental.ca</span>
      </li>
      <li class="contact__item">
        <svg class="contact__icon" viewBox="0 0 24 24" fill="none" stroke="var(--accent-yellow)" stroke-width="2"><rect x="3" y="5" width="18" height="14" rx="1"/><path d="M3 6l9 7 9-7"/></svg>
        <span>hello@corvantadental.ca</span>
      </li>
      <li class="contact__item">
        <svg class="contact__icon" viewBox="0 0 24 24" fill="var(--accent-yellow)"><path d="M12 2a7 7 0 0 0-7 7c0 5 7 13 7 13s7-8 7-13a7 7 0 0 0-7-7zm0 9.5a2.5 2.5 0 1 1 0-5 2.5 2.5 0 0 1 0 5z"/></svg>
        <span class="contact__address">204 – 1150 Marlow Ave<br>Winnipeg, MB R2K 3B8</span>
      </li>
    </ul>
    <p class="appointment__lead">Your Next Appointment is:</p>
    <div class="appointment__band">
      <div class="appointment__field"><span>Date</span><span class="appointment__line"></span></div>
      <div class="appointment__field appointment__field--time"><span>Time</span><span class="appointment__line"></span></div>
    </div>
    <p class="appointment__note">To cancel or reschedule please notify us at least 48 hours prior to your scheduled appointment.</p>
  </section>
</body>
</html>
```